Velora aesthetics offers a range of facial aesthetics treatments by a fully qualified dentist, to a high end crowd. Treatments include antiwrinkle treatment, the use of dermal fillers to provide facial volumisation and rejuvenation and also lip volumisation.
I want a luxurious and bold look. Black background with a bold striking gold logo in the centre possibly incorporating the outline of a face in a subtle yet effective way. I want it to include the work I offer so people will be aware of what they are looking into but not look like there's too much on the card, So it's a clean look.
At the bottom I would like it to say by Dr. Anjali Desai. Alongside my email address and mobile number.

```html
<!DOCTYPE html>
<html lang="en">
<head>
<meta charset="utf-8">
<title>Velora Aesthetics – Business Card</title>
<link rel="stylesheet" href="https://fonts.googleapis.com/css2?family=Montserrat:wght@500;700&family=Cormorant+Garamond:ital,wght@1,500&display=swap">
<style>
  :root {
    --backdrop: #d2ae63;
    --card-black: #0b0b0b;
    --gold: #d3a952;
    --gold-light: #f0cf7c;
    --gold-deep: #9c7328;
  }
  * { margin: 0; padding: 0; box-sizing: border-box; }
  html, body {
    width: 1200px;
    height: 1000px;
    overflow: hidden;
    background: var(--backdrop);
  }
  .canvas {
    position: relative;
    width: 1200px;
    height: 1000px;
  }
  .card {
    position: absolute;
    left: 98px;
    top: 175px;
    width: 1004px;
    height: 650px;
    background: var(--card-black);
    overflow: hidden;
  }
  .silhouette {
    position: absolute;
    top: 0;
    width: 192px;
    height: 330px;
  }
  .silhouette--left {
    left: 0;
    background: linear-gradient(100deg, var(--gold-light), var(--gold) 50%, var(--gold-deep));
    border-radius: 0 0 60% 0 / 0 0 30% 0;
  }
  .silhouette--right {
    right: 0;
    background: linear-gradient(260deg, var(--gold-light), var(--gold) 50%, var(--gold-deep));
    border-radius: 0 0 0 60% / 0 0 0 30%;
  }
  .flourish {
    position: absolute;
    background: radial-gradient(ellipse at center, rgba(211,169,82,0.55), rgba(211,169,82,0.12) 60%, rgba(211,169,82,0) 75%);
  }
  .flourish--top { left: 232px; top: 10px; width: 528px; height: 165px; }
  .flourish--bottom { left: 294px; top: 313px; width: 406px; height: 82px; }
  .brand {
    position: absolute;
    left: 0;
    width: 1004px;
    text-align: center;
    font-family: "Montserrat", sans-serif;
    font-weight: 700;
    color: var(--gold);
  }
  .brand__name {
    top: 180px;
    font-size: 80px;
    letter-spacing: 2px;
    line-height: 90px;
  }
  .brand__tagline {
    top: 262px;
    font-size: 30px;
    line-height: 40px;
    letter-spacing: 1px;
  }
  .practitioner {
    position: absolute;
    left: 0;
    top: 405px;
    width: 1004px;
    text-align: center;
    font-family: "Cormorant Garamond", serif;
    font-style: italic;
    font-weight: 500;
    font-size: 44px;
    color: var(--gold);
  }
  .info {
    position: absolute;
    top: 490px;
    font-family: "Montserrat", sans-serif;
    font-weight: 500;
    font-size: 24px;
    line-height: 32.5px;
    color: var(--gold);
    list-style: none;
  }
  .info--services { left: 34px; }
  .info--contact { left: 558px; }
</style>
</head>
<body>
  <main class="canvas">
    <section class="card">
      <div class="silhouette silhouette--left" role="img" aria-label="Gold illustration of a woman's profile with flowing hair"></div>
      <div class="silhouette silhouette--right" role="img" aria-label="Gold illustration of a woman's profile with flowing hair, mirrored"></div>

      <div class="flourish flourish--top" role="img" aria-label="Gold ornamental flourish above the name"></div>
      <h1 class="brand brand__name">VELORA</h1>
      <p class="brand brand__tagline">Aesthetics</p>
      <div class="flourish flourish--bottom" role="img" aria-label="Gold ornamental flourish below the name"></div>

      <p class="practitioner">By Dr. Anjali Desai (BDS)</p>

      <ul class="info info--services">
        <li>Specialist in :</li>
        <li>Antiwrinkle treatment</li>
        <li>Lips and Facial Volumisation</li>
        <li>and Rejuvenation</li>
      </ul>

      <ul class="info info--contact">
        <li>Contact Details :</li>
        <li>ad@veloraaesthetics.com</li>
        <li>07700900123</li>
        <li>www.veloraaesthetics.com</li>
      </ul>
    </section>
  </main>
</body>
</html>
```